Business Card Design

We require a business card design for a law firm, our signature colours are maroon and cream. Our slogan is "From our family to yours", we would like the cards to be professional however feminine at the same time.

Industry/Entity Type

Business

Contact Information for Business Card

Helena Brackett & Associates Lawyers & Conveyancers, Helena Brackett LL.B. Principal Solicitor, 17 Quillon Street, Marrowdale NSW 2190

Logo styles of interest
Emblem Logo
Abstract Logo
Wordmark Logo

```html
<!DOCTYPE html>
<html lang="en">
<head>
<meta charset="utf-8">
<title>Helena Brackett &amp; Associates – Business Card</title>
<link rel="stylesheet" href="https://fonts.googleapis.com/css2?family=EB+Garamond:wght@400;500;600;700&display=swap">
<style>
  :root {
    --maroon: #8d2a34;
    --band: #922b34;
    --paper: #ffffff;
    --on-band: #fbf4ec;
  }
  * { margin: 0; padding: 0; box-sizing: border-box; }
  html, body {
    width: 1200px;
    height: 695px;
    overflow: hidden;
    background: var(--paper);
  }
  .card {
    position: relative;
    width: 1200px;
    height: 695px;
    background: var(--paper);
    font-family: "EB Garamond", Georgia, serif;
    color: var(--maroon);
  }
  .brand-mark {
    position: absolute;
    top: 110px;
    left: 0;
    width: 100%;
    display: flex;
    justify-content: center;
    align-items: center;
    gap: 14px;
  }
  .brand-mark__dot {
    width: 26px;
    height: 26px;
    border-radius: 50%;
    background: var(--maroon);
  }
  .brand-mark__name {
    font-size: 34px;
    font-weight: 600;
    color: var(--maroon);
    letter-spacing: 0.5px;
  }
  .firm-name {
    position: absolute;
    top: 268px;
    left: 0;
    width: 100%;
    text-align: center;
    font-size: 49px;
    font-weight: 600;
    line-height: 70px;
    letter-spacing: 0.3px;
  }
  .slogan {
    position: absolute;
    top: 436px;
    left: 0;
    width: 100%;
    text-align: center;
    font-size: 29px;
    font-weight: 400;
    letter-spacing: 0.6px;
    text-transform: uppercase;
  }
  .contact-band {
    position: absolute;
    left: 0;
    top: 523px;
    width: 1200px;
    height: 172px;
    background: var(--band);
    color: var(--on-band);
  }
  .person-name {
    position: absolute;
    left: 45px;
    top: 36px;
    font-size: 39px;
    font-weight: 600;
    letter-spacing: 0.2px;
  }
  .person-role {
    position: absolute;
    left: 45px;
    top: 99px;
    font-size: 33px;
    font-weight: 400;
  }
  .address {
    position: absolute;
    right: 34px;
    top: 105px;
    font-size: 27px;
    font-weight: 400;
    font-style: normal;
    letter-spacing: 0.4px;
  }
</style>
</head>
<body>
  <main class="card">
    <div class="brand-mark">
      <span class="brand-mark__dot"></span>
      <span class="brand-mark__name">Helena Brackett</span>
    </div>

    <h1 class="firm-name">Helena Brackett &amp; Associates<br>Lawyers &amp; Conveyancers</h1>

    <p class="slogan">From our family to yours</p>

    <section class="contact-band">
      <p class="person-name">Helena Brackett LL.B.</p>
      <p class="person-role">Principal Solicitor</p>
      <address class="address">17 Quillon Street, Marrowdale NSW 2190</address>
    </section>
  </main>
</body>
</html>
```